Home Page Design

Please see design brief attached. Concept here: sketchboard[dot]io/file/qWm83LzpR7cvXuNtYa2KhE/Brindlemoor---Landing-Page?node-id=0%3A1&t=PKr92mvnQsD4xTcZ-1

Industry/Entity Type

Wedding

Number of Pages Required

1 page

Font styles to use
Serif
Sans Serif
Decorative
Script

Colors
A7469A
B969AE
D3A5CF
EDDBEB
F8F0F9
6B429C
8869AF
B7A5CE
E3DAEB
F3F0F8

Requirements
Must have
• Please see attached PDF
Nice to have
• Please see attached PDF
Should not have
• Please see attached PDF

```html
<!DOCTYPE html>
<html lang="en">
<head>
<meta charset="utf-8">
<title>Brindlemoor — Wedding Vendors</title>
<link href="https://fonts.googleapis.com/css2?family=Playfair+Display:wght@500;600;700&family=Poppins:wght@300;400;500;600&display=swap" rel="stylesheet">
<style>
:root{
  --plum:#5E2A72;
  --plum-deep:#4E2261;
  --orchid:#A7469A;
  --orchid-soft:#B969AE;
  --lilac:#D3A5CF;
  --blush:#EDDBEB;
  --mist:#F8F0F9;
  --violet:#6B429C;
  --lavender:#E3DAEB;
  --grey-band:#EFEFF1;
  --ink:#2B2330;
  --muted:#77707C;
  --white:#FFFFFF;
}
*{box-sizing:border-box;margin:0;padding:0}
html,body{width:1200px;height:3444px;overflow:hidden}
body{font-family:"Poppins",sans-serif;color:var(--ink);background:var(--white);font-size:14px}
h1,h2,h3,.serif{font-family:"Playfair Display",serif}

/* Header */
.site-header{height:120px;position:relative;background:var(--white)}
.couple-select{position:absolute;left:112px;top:26px;width:118px;height:30px;border:1px solid #ddd;border-radius:3px;font-size:11px;display:flex;align-items:center;padding:0 10px;justify-content:space-between;color:var(--muted)}
.brand{position:absolute;left:0;right:0;top:18px;text-align:center;font-family:"Playfair Display",serif;font-size:26px;font-weight:600;color:var(--plum)}
.auth{position:absolute;right:112px;top:26px;display:flex;gap:8px}
.auth a{height:30px;padding:0 14px;font-size:11px;display:flex;align-items:center;border-radius:3px;text-decoration:none}
.auth .login{background:var(--blush);color:var(--plum)}
.auth .signup{background:var(--plum);color:var(--white)}
.main-nav{position:absolute;left:0;right:0;top:84px;display:flex;justify-content:center;gap:38px;font-size:12px}
.main-nav a{color:var(--ink);text-decoration:none}
.main-nav a.active{color:var(--orchid);font-weight:600}

/* Hero */
.hero{height:520px;position:relative;background:linear-gradient(100deg,#d9dde3 0%,#c8ccd2 40%,#b7a5a2 70%,#e7e1dc 100%)}
.hero-photo{position:absolute;inset:0}
.hero-card{position:absolute;left:112px;top:60px;width:360px;height:340px;background:var(--white);padding:34px 32px;box-shadow:0 8px 24px rgba(0,0,0,.08)}
.hero-card h1{font-size:30px;line-height:1.2;font-weight:600;color:var(--ink)}
.hero-card p{font-size:11px;color:var(--muted);margin-top:10px;line-height:1.5}
.field{margin-top:14px;border-bottom:1px solid #ddd;padding-bottom:6px}
.field small{display:block;font-size:9px;color:var(--muted)}
.field span{font-size:12px}
.btn{display:inline-block;background:var(--plum);color:var(--white);font-size:12px;padding:9px 20px;border-radius:2px;text-decoration:none}
.hero-card .btn{position:absolute;right:32px;bottom:30px}

/* Section titles */
.section-title{font-size:32px;font-weight:600;display:flex;align-items:center;gap:10px}
.section-title::after{content:"";width:26px;height:1px;background:var(--ink)}

/* Vendors */
.vendors{height:840px;position:relative;padding:100px 112px 0}
.vendors .view-all{position:absolute;right:112px;top:104px;padding:8px 22px}
.vendor-grid{display:grid;grid-template-columns:repeat(4,190px);justify-content:space-between;row-gap:56px;margin-top:52px;padding:0 28px}
.vendor{text-align:center}
.vendor-ring{width:190px;height:190px;border-radius:50%;border:3px solid var(--plum);padding:6px;position:relative}
.vendor-photo{width:100%;height:100%;border-radius:50%}
.vendor-badge{position:absolute;left:50%;bottom:-14px;transform:translateX(-50%);width:36px;height:36px;border-radius:50%;background:var(--plum);border:3px solid var(--white);display:flex;align-items:center;justify-content:center}
.vendor-name{margin-top:26px;font-size:15px;font-weight:500}

/* Categories */
.categories{height:380px;background:var(--grey-band);padding:60px 112px 0;position:relative}
.cat-row{display:grid;grid-template-columns:repeat(4,1fr);gap:16px;margin-top:34px}
.cat-card{height:220px;display:flex;flex-direction:column}
.cat-photo{flex:1}
.cat-label{height:36px;background:var(--plum);color:var(--white);font-size:13px;display:flex;align-items:center;justify-content:center}
.cat-card.active .cat-label{background:var(--orchid-soft)}
.slider-arrow{position:absolute;font-size:22px;color:var(--muted)}

/* Testimonials */
.testimonials{height:430px;background:#F4F4F5;margin-top:30px;position:relative;padding:50px 0 0}
.testimonials .section-title{justify-content:center}
.quote-box{position:absolute;left:260px;top:150px;width:680px;height:220px;background:var(--white);border:1px solid #ccc;padding:30px 36px}
.quote-box h3{font-size:32px;font-weight:600}
.quote-box p{font-size:10px;color:var(--muted);line-height:1.6;width:330px;margin-top:14px}
.quote-box .who{font-size:9px;font-weight:600;margin-top:8px}
.quote-box .btn{margin-top:14px;font-size:11px;padding:7px 16px}
.quote-photo{position:absolute;right:28px;top:-18px;width:230px;height:220px}

/* Steps */
.steps{height:390px;position:relative;padding:70px 112px 0}
.steps .section-title{margin-left:100px}
.step-row{display:flex;justify-content:space-between;width:700px;margin:40px auto 0;position:relative}
.step-row::before{content:"";position:absolute;left:72px;right:72px;top:72px;height:2px;background:var(--plum)}
.step{text-align:center;width:200px;position:relative}
.step-circle{width:144px;height:144px;border-radius:50%;border:3px solid var(--plum);background:var(--white);margin:0 auto;display:flex;align-items:center;justify-content:center;position:relative}
.step-num{position:absolute;left:-14px;top:56px;width:30px;height:30px;border-radius:50%;background:var(--plum);color:var(--white);font-size:13px;display:flex;align-items:center;justify-content:center}
.step p{margin-top:16px;font-size:14px;font-weight:500}

/* Features */
.features{height:360px;background:var(--mist);padding:80px 0 0;position:relative}
.features .section-title{justify-content:center}
.feature-row{display:flex;justify-content:center;gap:18px;margin-top:50px}
.feature{width:112px;height:100px;background:var(--white);box-shadow:0 2px 8px rgba(0,0,0,.08);display:flex;flex-direction:column;align-items:center;justify-content:center;gap:12px;font-size:11px}

/* Footer */
.site-footer{height:324px;background:var(--plum);color:var(--white);padding:60px 112px 0;position:relative}
.foot-cols{display:flex;gap:120px;margin-left:96px}
.foot-col h4{font-size:12px;font-weight:600;margin-bottom:16px;letter-spacing:.3px}
.foot-col li{list-style:none;font-size:11px;margin-bottom:9px;opacity:.9}
.social{position:absolute;right:140px;top:60px;display:flex;flex-direction:column;gap:10px}
.social span{width:28px;height:28px;background:var(--white);display:block}
.foot-bottom{position:absolute;left:112px;right:112px;bottom:26px;display:flex;justify-content:space-between;font-size:10px;border-top:1px solid rgba(255,255,255,.2);padding-top:14px}
</style>
</head>
<body>

<header class="site-header">
  <div class="couple-select">Find A Couple <span>▾</span></div>
  <div class="brand">Brindlemoor</div>
  <div class="auth"><a class="login" href="#">Log in</a><a class="signup" href="#">Sign Up</a></div>
  <nav class="main-nav">
    <a class="active" href="#">Home</a><a href="#">Planning Tools</a><a href="#">Vendors</a><a href="#">Wedding Website</a><a href="#">Invitations</a><a href="#">Registry</a><a href="#">Ideas &amp; Blogs</a><a href="#">Gifts &amp; Favors</a>
  </nav>
</header>

<section class="hero">
  <div class="hero-photo" role="img" aria-label="Photo of a bride and groom embracing outdoors with white bunting overhead"></div>
  <div class="hero-card">
    <h1>Meet Your Wedding Vendor Team</h1>
    <p>Find And Book The Best Wedding Vendors With Help From The Pros</p>
    <div class="field"><small>Category</small><span>Reception Venues</span></div>
    <div class="field"><small>City, State</small><span>Woodhaven, PA</span></div>
    <a class="btn" href="#">Search</a>
  </div>
</section>

<section class="vendors">
  <h2 class="section-title">Featuring Featured Vendors</h2>
  <a class="btn view-all" href="#">View All</a>
  <div class="vendor-grid">
    <div class="vendor"><div class="vendor-ring"><div class="vendor-photo" style="background:linear-gradient(135deg,#9c9aa0,#d8d2cc)" role="img" aria-label="Reception venue with set tables"></div><div class="vendor-badge"><svg width="16" height="16" viewBox="0 0 16 16"><path d="M2 14V6l6-4 6 4v8H2z" fill="none" stroke="#fff" stroke-width="1.6"/></svg></div></div><div class="vendor-name">Reception Venues</div></div>
    <div class="vendor"><div class="vendor-ring"><div class="vendor-photo" style="background:linear-gradient(135deg,#7b6d62,#cdb9a5)" role="img" aria-label="Photographer at a wedding"></div><div class="vendor-badge"><svg width="16" height="16" viewBox="0 0 16 16"><rect x="2" y="5" width="12" height="8" rx="1" fill="none" stroke="#fff" stroke-width="1.6"/><circle cx="8" cy="9" r="2" fill="#fff"/></svg></div></div><div class="vendor-name">Wedding Photographers</div></div>
    <div class="vendor"><div class="vendor-ring"><div class="vendor-photo" style="background:linear-gradient(135deg,#b08a7a,#e6d8d0)" role="img" aria-label="Videographer filming a ceremony"></div><div class="vendor-badge"><svg width="16" height="16" viewBox="0 0 16 16"><rect x="2" y="5" width="8" height="7" fill="none" stroke="#fff" stroke-width="1.6"/><path d="M10 8l4-2v5l-4-2z" fill="#fff"/></svg></div></div><div class="vendor-name">Videographers</div></div>
    <div class="vendor"><div class="vendor-ring"><div class="vendor-photo" style="background:linear-gradient(135deg,#6b4fa8,#c4a6e0)" role="img" aria-label="DJ performing under purple lights"></div><div class="vendor-badge"><svg width="16" height="16" viewBox="0 0 16 16"><circle cx="8" cy="8" r="5" fill="none" stroke="#fff" stroke-width="1.6"/><circle cx="8" cy="8" r="1.5" fill="#fff"/></svg></div></div><div class="vendor-name">DJS</div></div>
    <div class="vendor"><div class="vendor-ring"><div class="vendor-photo" style="background:linear-gradient(135deg,#3d3d3f,#a3a3a5)" role="img" aria-label="Wedding band playing live"></div><div class="vendor-badge"><svg width="16" height="16" viewBox="0 0 16 16"><path d="M6 12V3l7-1v9" fill="none" stroke="#fff" stroke-width="1.6"/><circle cx="4.5" cy="12" r="1.8" fill="#fff"/><circle cx="11.5" cy="11" r="1.8" fill="#fff"/></svg></div></div><div class="vendor-name">Wedding Bands</div></div>
    <div class="vendor"><div class="vendor-ring"><div class="vendor-photo" style="background:linear-gradient(135deg,#6f5a44,#c8b291)" role="img" aria-label="Wedding planner arranging decor"></div><div class="vendor-badge"><svg width="16" height="16" viewBox="0 0 16 16"><rect x="3" y="3" width="10" height="11" fill="none" stroke="#fff" stroke-width="1.6"/><path d="M5 7h6M5 10h6" stroke="#fff" stroke-width="1.4"/></svg></div></div><div class="vendor-name">Wedding Planners</div></div>
    <div class="vendor"><div class="vendor-ring"><div class="vendor-photo" style="background:linear-gradient(135deg,#c9a9a0,#f2e6e1)" role="img" aria-label="Wedding rings on petals"></div><div class="vendor-badge"><svg width="16" height="16" viewBox="0 0 16 16"><path d="M3 6l2-3h6l2 3-5 7z" fill="none" stroke="#fff" stroke-width="1.5"/></svg></div></div><div class="vendor-name">Jewelers</div></div>
    <div class="vendor"><div class="vendor-ring"><div class="vendor-photo" style="background:linear-gradient(135deg,#d9d4d0,#f7f4f1)" role="img" aria-label="Tiered white wedding cake"></div><div class="vendor-badge"><svg width="16" height="16" viewBox="0 0 16 16"><rect x="3" y="9" width="10" height="5" fill="none" stroke="#fff" stroke-width="1.5"/><rect x="5" y="5" width="6" height="4" fill="none" stroke="#fff" stroke-width="1.5"/></svg></div></div><div class="vendor-name">Wedding Cakes</div></div>
  </div>
</section>

<section class="categories">
  <h2 class="section-title">Popular Wedding Categories</h2>
  <span class="slider-arrow" style="left:80px;top:200px">‹</span>
  <span class="slider-arrow" style="right:80px;top:200px">›</span>
  <div class="cat-row">
    <div class="cat-card"><div class="cat-photo" style="background:linear-gradient(135deg,#a28e84,#e8ddd6)" role="img" aria-label="Florist arranging a bouquet"></div><div class="cat-label">Florists</div></div>
    <div class="cat-card active"><div class="cat-photo" style="background:linear-gradient(135deg,#8c7c73,#efe6e0)" role="img" aria-label="Bridal accessories laid out"></div><div class="cat-label">Bridal Lehenga</div></div>
    <div class="cat-card"><div class="cat-photo" style="background:linear-gradient(135deg,#b7868a,#ead0d0)" role="img" aria-label="Bride trying gowns in a bridal salon"></div><div class="cat-label">Bridal Salons</div></div>
    <div class="cat-card"><div class="cat-photo" style="background:linear-gradient(135deg,#c7bfb6,#f1ece6)" role="img" aria-label="Bright hotel room with a made bed"></div><div class="cat-label">Hotel Room Blocks</div></div>
  </div>
</section>

<section class="testimonials">
  <h2 class="section-title">Testimonials</h2>
  <span class="slider-arrow" style="left:200px;top:240px">‹</span>
  <span class="slider-arrow" style="right:200px;top:240px">›</span>
  <div class="quote-box">
    <h3>What Our Clients Say</h3>
    <p>Planning our day felt calm from the first search. We found a florist, a band and a venue within one week, and every vendor answered quickly and kindly. The booking tools kept our budget clear and our guests informed.</p>
    <div class="who">Rosalind &amp; Theo Varga</div>
    <a class="btn" href="#">Read More</a>
    <div class="quote-photo" style="background:linear-gradient(135deg,#b79a92,#efe4e0)" role="img" aria-label="Portrait of a smiling bride in a veil"></div>
  </div>
</section>

<section class="steps">
  <h2 class="section-title">Finding A Wedding Vendor</h2>
  <div class="step-row">
    <div class="step"><div class="step-circle"><span class="step-num">1</span><svg width="56" height="56" viewBox="0 0 56 56" fill="none" stroke="#5E2A72" stroke-width="2.2"><rect x="8" y="10" width="40" height="28" rx="2"/><circle cx="20" cy="46" r="4"/><circle cx="36" cy="46" r="4"/><path d="M16 24h24"/></svg></div><p>Start With Your Style</p></div>
    <div class="step"><div class="step-circle"><span class="step-num">2</span><svg width="56" height="56" viewBox="0 0 56 56" fill="none" stroke="#5E2A72" stroke-width="2.2"><rect x="8" y="8" width="14" height="14"/><rect x="34" y="8" width="14" height="14"/><rect x="8" y="34" width="14" height="14"/><path d="M34 34l10 10M40 32v10h8"/></svg></div><p>Understand The Options</p></div>
    <div class="step"><div class="step-circle"><span class="step-num">3</span><svg width="56" height="56" viewBox="0 0 56 56" fill="none" stroke="#5E2A72" stroke-width="2.2"><path d="M6 10h26v16H16l-6 6V26H6z"/><path d="M50 24H28v16h14l6 6v-6h2z"/></svg></div><p>Start A Conversation</p></div>
  </div>
</section>

<section class="features">
  <h2 class="section-title">Features / Benefits</h2>
  <div class="feature-row">
    <div class="feature"><svg width="28" height="28" viewBox="0 0 28 28" fill="none" stroke="#5E2A72" stroke-width="1.8"><path d="M4 24V11l10-7 10 7v13z"/></svg>Wedding Venues</div>
    <div class="feature"><svg width="28" height="28" viewBox="0 0 28 28" fill="none" stroke="#5E2A72" stroke-width="1.8"><rect x="4" y="7" width="20" height="15"/><path d="M4 7l10 8 10-8"/></svg>Invitations</div>
    <div class="feature"><svg width="28" height="28" viewBox="0 0 28 28" fill="none" stroke="#5E2A72" stroke-width="1.8"><rect x="3" y="5" width="22" height="16"/><path d="M10 25h8M14 21v4"/></svg>Wedding Website</div>
    <div class="feature"><svg width="28" height="28" viewBox="0 0 28 28" fill="none" stroke="#5E2A72" stroke-width="1.8"><rect x="5" y="4" width="18" height="21"/><path d="M9 10h10M9 15h10M9 20h6"/></svg>Planner</div>
    <div class="feature"><svg width="28" height="28" viewBox="0 0 28 28" fill="none" stroke="#5E2A72" stroke-width="1.8"><path d="M14 4a7 7 0 0 0-4 13v3h8v-3a7 7 0 0 0-4-13zM11 24h6"/></svg>Ideas</div>
    <div class="feature"><svg width="28" height="28" viewBox="0 0 28 28" fill="none" stroke="#5E2A72" stroke-width="1.8"><path d="M9 4h10l-2 8h-6zM14 12v12M9 24h10"/></svg>Wedding Dresses</div>
  </div>
</section>

<footer class="site-footer">
  <div class="foot-cols">
    <div class="foot-col"><h4>QUICK LINKS</h4><ul><li>Home</li><li>Planning Tools</li><li>Vendors</li><li>Wedding Website</li><li>Registry</li></ul></div>
    <div class="foot-col"><h4>OTHER LINK</h4><ul><li>Gifts &amp; Favors</li><li>Ideas &amp; Blogs</li><li>Invitations</li><li>Ideas</li><li>FAQ</li></ul></div>
    <div class="foot-col"><h4>CONTACT US</h4><ul><li>214 Lantern Row, Suite 8,</li><li>Marlow Heights, PA</li><li>(555) 014-2290</li><li>hello@brindlemoorevents.com</li></ul></div>
  </div>
  <div class="social" aria-label="Social links"><span></span><span></span><span></span><span></span></div>
  <div class="foot-bottom"><span>© 2023 Brindlemoor, All Rights Reserved.</span><span>Terms Of Service</span></div>
</footer>

</body>
</html>
```